Revamp Current Website From 2012 TO 2018

We need a ravamp to our current website. I prefer a professional corporate modern feel to it.

My Current Website is www.brightlanepromoworks.biz. Please redesign the homepage and the /certs page first....see attached document for specific instructions..

There is a lot of content at the bottom but maybe we can shorten that by using titles and a pop up of the details or something so it doesnt take too mcuh space...or maybe a red more hyperlink to see the rest of info in pop up or something or new page...

Target Market(s)

B2B, business owners, website owners, marketing companies.

Industry/Entity Type

Promotional Product

Number of Pages Required

2 page

Colors

Designer to choose colors to be used in the design.

Requirements
Must have
• Please keep in mind logo mock up I am working on that looks beautiful on dark background for header...see attached for logo
• Must use existing content I hope your marketing mind comes in to play when designing the website.
• Must have all my content provided on each page...
Nice to have
• similiar color scheme...
Should not have
• I dont like using templates because usually hard to expand on design in Northpeak so Prefer full custom designs
• Please no templates

```html
<!DOCTYPE html>
<html lang="en">
<head>
<meta charset="utf-8">
<title>Brightlane Promoworks</title>
<link href="https://fonts.googleapis.com/css2?family=Open+Sans:wght@400;600;700;800&display=swap" rel="stylesheet">
<style>
:root{
  --ink:#3a3a3a;
  --muted:#666;
  --blue:#0a6fc2;
  --blue-dark:#0650a6;
  --blue-light:#0b8fe0;
  --header:#1c1c1e;
  --nav:#2d2a28;
  --footer:#1a1a1b;
  --white:#fff;
  --line:#d7d7d7;
}
*{box-sizing:border-box;margin:0;padding:0}
html,body{width:1200px;height:3175px;overflow:hidden}
body{font-family:"Open Sans",Arial,sans-serif;color:var(--ink);background:#fff}
.wrap{width:1000px;margin:0 auto;position:relative}
a{color:inherit;text-decoration:none}

/* header */
.site-header{height:201px;background:var(--header)}
.site-header .wrap{height:201px;display:flex;align-items:center;justify-content:space-between}
.brand{display:flex;align-items:center;gap:16px;color:var(--blue-light);font-weight:800;font-size:34px;letter-spacing:.5px;text-transform:uppercase}
.brand-square{width:46px;height:46px;background:var(--blue-light)}
.contact-top{color:var(--white);margin-top:-20px}
.contact-top small{display:block;color:var(--blue-light);font-size:13px;font-weight:600;margin-bottom:4px}
.contact-top .num{font-size:27px;font-weight:600;display:flex;align-items:center;gap:8px;margin-bottom:22px}

/* nav */
.main-nav{height:57px;background:var(--nav)}
.main-nav ul{list-style:none;display:flex;height:57px}
.main-nav li{color:var(--white);font-size:14px;font-weight:600;text-transform:uppercase;padding:0 21px;display:flex;align-items:center}
.main-nav li.active{background:var(--blue)}

/* hero */
.hero{height:542px;position:relative;background:linear-gradient(135deg,#5a4a3c 0%,#8a7560 30%,#6e5f50 60%,#4a3e34 100%);color:var(--white);text-align:center}
.hero::after{content:"";position:absolute;inset:0;background:rgba(20,20,25,.35)}
.hero-inner{position:relative;z-index:1;padding-top:112px}
.hero h1{font-size:27px;font-weight:800;line-height:1.35}
.hero p{font-size:13.5px;line-height:1.5;width:1000px;margin:10px auto 0}
.ticks{list-style:none;display:inline-block;text-align:left;margin-top:14px}
.ticks li{font-size:13.5px;font-weight:600;display:flex;align-items:center;gap:10px;line-height:25px}
.btn-solid{display:inline-block;background:var(--blue);color:var(--white);font-weight:600;font-size:22px;padding:12px 36px;letter-spacing:.5px}
.hero .btn-solid{margin-top:18px}
.hero-arrow{position:absolute;top:230px;z-index:1;color:var(--white);font-size:30px}

/* ways */
.ways{height:618px;text-align:center;padding-top:75px}
.section-title{font-size:31px;font-weight:700;line-height:1.25;text-transform:uppercase;color:#404040}
.ways-grid{display:flex;justify-content:space-between;margin-top:55px}
.way{width:300px;display:flex;flex-direction:column;align-items:center}
.way-icon{width:148px;height:148px;border-radius:50%;background:var(--blue);border:6px solid #fff;box-shadow:0 0 0 4px var(--blue);display:flex;align-items:center;justify-content:center}
.way h3{font-size:19px;font-weight:400;margin-top:20px;line-height:1.3;min-height:52px;display:flex;align-items:center}
.way p{font-size:12px;color:var(--muted);line-height:1.45;margin-top:6px;min-height:90px}
.btn-line{display:inline-block;border:2px solid var(--blue);color:var(--blue);font-size:16px;font-weight:600;padding:9px 22px;text-transform:uppercase}

/* distribution */
.distribution{height:607px;background:linear-gradient(180deg,var(--blue-light) 0%,var(--blue-dark) 100%);color:var(--white);text-align:center;padding-top:68px}
.distribution .section-title{color:var(--white)}
.slider-ctrl{position:absolute;right:0;top:0;display:flex;gap:6px}
.slider-ctrl span{width:24px;height:24px;border:1px solid #fff;display:flex;align-items:center;justify-content:center;font-size:14px}
.dist-grid{display:flex;justify-content:space-between;margin-top:48px}
.dist-card{width:303px}
.dist-photo{height:159px;border:4px solid #fff}
.dist-card h3{font-size:25px;font-weight:600;margin-top:20px}
.dist-card p{font-size:14px;line-height:1.45;margin-top:6px;height:62px}
.distribution .btn-line{border-color:#fff;color:#fff;margin-top:14px}

/* pricing */
.pricing{height:504px;text-align:center;padding-top:65px}
.pricing .section-title{font-size:30px}
.pricing p{font-size:13px;line-height:1.5;color:#444;margin-top:26px;padding:0 30px}
.pricing p+p{margin-top:22px}
.pricing .btn-solid{font-size:15px;padding:14px 24px;margin-top:28px;background:var(--blue-dark)}

/* clients */
.clients{height:307px;text-align:center;padding-top:38px}
.client-row{display:flex;justify-content:space-between;align-items:center;margin-top:52px;position:relative}
.client-logo{width:154px;height:93px;border:1px solid var(--line);display:flex;align-items:center;justify-content:center;font-size:14px;font-weight:700;color:#444}
.client-arrow{position:absolute;top:28px;color:#bbb;font-size:28px}

/* footer */
.site-footer{height:339px;background:var(--footer);color:var(--white);padding-top:36px}
.foot-cols{display:flex}
.foot-col h4{font-size:18px;font-weight:600;text-transform:uppercase;margin-bottom:16px}
.links{width:357px;border-right:1px solid #444;height:200px}
.links ul{list-style:none;columns:2;width:260px}
.links li{font-size:14px;line-height:32px}
.contact{width:320px;padding-left:30px;border-right:1px solid #444;height:200px;font-size:14px;line-height:29px}
.contact .row{display:flex;align-items:center;gap:10px}
.news{padding-left:45px;flex:1}
.news p{font-size:13px}
.sub-form{display:flex;margin-top:12px}
.sub-form span{width:226px;height:40px;background:#fff;color:#aaa;font-size:12px;display:flex;align-items:center;padding-left:14px}
.sub-form b{background:var(--blue);height:40px;padding:0 16px;display:flex;align-items:center;font-size:14px}
.socials{display:flex;gap:14px;margin-top:22px}
.socials span{width:38px;height:38px;border-radius:50%;background:#fff}
.copyright{border-top:1px solid #444;margin-top:50px;padding-top:20px;font-size:14px}
</style>
</head>
<body>

<header class="site-header">
  <div class="wrap">
    <div class="brand"><span class="brand-square"></span>Brightlane Promoworks</div>
    <div class="contact-top">
      <small>USA Office</small>
      <div class="num"><svg width="22" height="22" viewBox="0 0 24 24" fill="#fff"><path d="M6.6 10.8a15 15 0 0 0 6.6 6.6l2.2-2.2a1 1 0 0 1 1-.25 11.4 11.4 0 0 0 3.6.6 1 1 0 0 1 1 1V20a1 1 0 0 1-1 1A17 17 0 0 1 3 4a1 1 0 0 1 1-1h3.5a1 1 0 0 1 1 1c0 1.25.2 2.45.6 3.6a1 1 0 0 1-.25 1z"/></svg>619-555-0148</div>
      <small>International</small>
      <div class="num" style="margin-bottom:0"><svg width="22" height="22" viewBox="0 0 24 24" fill="#fff"><path d="M6.6 10.8a15 15 0 0 0 6.6 6.6l2.2-2.2a1 1 0 0 1 1-.25 11.4 11.4 0 0 0 3.6.6 1 1 0 0 1 1 1V20a1 1 0 0 1-1 1A17 17 0 0 1 3 4a1 1 0 0 1 1-1h3.5a1 1 0 0 1 1 1c0 1.25.2 2.45.6 3.6a1 1 0 0 1-.25 1z"/></svg>1-800-555-0192</div>
    </div>
  </div>
</header>

<nav class="main-nav">
  <div class="wrap">
    <ul>
      <li class="active">Home</li><li>Our Incentives</li><li>Samples</li><li>How It Works</li><li>Testimonials</li><li>FAQ</li><li>Contact</li><li>Sign Up</li><li>Log In</li>
    </ul>
  </div>
</nav>

<section class="hero" role="img" aria-label="Team around a wooden desk with laptops, coffee cups and colour swatches">
  <span class="hero-arrow" style="left:38px">&#8249;</span>
  <span class="hero-arrow" style="right:38px">&#8250;</span>
  <div class="hero-inner">
    <h1>Increase Leads &amp; Sales From Your Existing Marketing Efforts By Offering<br>High Perceived Value Incentives To Your Customers!</h1>
    <p>Create a variety giveaway promotions for your business with an unlimited supply of top quality vacation getaway certificates, restaurant gift certificates, electronic product giveaways and gas or grocery rewards for just $99/mth. Whether you need 100 or 100,000 you will never pay more than $99.</p>
    <ul class="ticks">
      <li><svg width="14" height="14" viewBox="0 0 14 14"><circle cx="7" cy="7" r="7" fill="#fff"/><path d="M3.5 7.2l2.3 2.2 4.7-4.8" stroke="#333" stroke-width="1.8" fill="none"/></svg>12 Years In Business</li>
      <li><svg width="14" height="14" viewBox="0 0 14 14"><circle cx="7" cy="7" r="7" fill="#fff"/><path d="M3.5 7.2l2.3 2.2 4.7-4.8" stroke="#333" stroke-width="1.8" fill="none"/></svg>13,000+ Clients Enrolled</li>
      <li><svg width="14" height="14" viewBox="0 0 14 14"><circle cx="7" cy="7" r="7" fill="#fff"/><path d="M3.5 7.2l2.3 2.2 4.7-4.8" stroke="#333" stroke-width="1.8" fill="none"/></svg>2+ Million Certificates In Circulation</li>
      <li><svg width="14" height="14" viewBox="0 0 14 14"><circle cx="7" cy="7" r="7" fill="#fff"/><path d="M3.5 7.2l2.3 2.2 4.7-4.8" stroke="#333" stroke-width="1.8" fill="none"/></svg>170,000 + Redemptions To Date</li>
      <li><svg width="14" height="14" viewBox="0 0 14 14"><circle cx="7" cy="7" r="7" fill="#fff"/><path d="M3.5 7.2l2.3 2.2 4.7-4.8" stroke="#333" stroke-width="1.8" fill="none"/></svg>A Rating BTC</li>
      <li><svg width="14" height="14" viewBox="0 0 14 14"><circle cx="7" cy="7" r="7" fill="#fff"/><path d="M3.5 7.2l2.3 2.2 4.7-4.8" stroke="#333" stroke-width="1.8" fill="none"/></svg>Licensed Seller Of Travel CST #4470318</li>
    </ul>
    <div><span class="btn-solid">30 DAY RISK FREE TRIAL</span></div>
  </div>
</section>

<section class="ways">
  <div class="wrap">
    <h2 class="section-title">We Plug Right Into Your Existing Business<br>Model In 4 Ways:</h2>
    <div class="ways-grid">
      <div class="way">
        <div class="way-icon"><svg width="64" height="64" viewBox="0 0 64 64" fill="none" stroke="#fff" stroke-width="4" stroke-linejoin="round"><path d="M10 26h10l22-12v36L20 38H10z"/><path d="M18 38l4 14h7l-3-14"/><path d="M50 24l6-4M50 32h8M50 40l6 4"/></svg></div>
        <h3>Boost Response Rates To<br>Your Existing Ads</h3>
        <p>By adding one extra tagline: "Call for a Free Quote and receive a Three Day Two Night Hotel Stay Certificate to Las Vegas or 50 + other popular destinations, No Purchase Necessary."</p>
        <span class="btn-line">Read More</span>
      </div>
      <div class="way">
        <div class="way-icon"><svg width="72" height="64" viewBox="0 0 72 64" fill="#fff"><circle cx="20" cy="14" r="6"/><circle cx="36" cy="10" r="6"/><circle cx="52" cy="14" r="6"/><path d="M10 34c0-8 20-8 20 0zM26 30c0-8 20-8 20 0zM42 34c0-8 20-8 20 0z"/><path d="M6 54l22-10 12 6 20-14" stroke="#fff" stroke-width="4" fill="none"/><path d="M56 30l10 2-4 9z"/></svg></div>
        <h3>Get More New Customers</h3>
        <p>Now that you have generated a new lead, try enticing them with an upgrade and offer them Two Nights Plus Airfare if they purchase today.</p>
        <span class="btn-line">Read More</span>
      </div>
      <div class="way">
        <div class="way-icon"><svg width="66" height="64" viewBox="0 0 66 64" fill="#fff"><circle cx="33" cy="12" r="7"/><path d="M22 30c0-11 22-11 22 0z"/><path d="M33 32v8M12 40h42M12 40v6M54 40v6M33 40v6" stroke="#fff" stroke-width="3"/><circle cx="12" cy="50" r="5"/><circle cx="33" cy="50" r="5"/><circle cx="54" cy="50" r="5"/><path d="M4 64c0-8 16-8 16 0zM25 64c0-8 16-8 16 0zM46 64c0-8 16-8 16 0z"/></svg></div>
        <h3>Increase Repeat &amp; Referral<br>Business</h3>
        <p>Remind past clients about your products &amp; services with a 7 Night Resort Getaway in one of over 3500 destinations around the world to motivate repeat business.</p>
        <span class="btn-line">Read More</span>
      </div>
    </div>
  </div>
</section>

<section class="distribution">
  <div class="wrap">
    <h2 class="section-title">Easy Distribution</h2>
    <div class="slider-ctrl" style="top:32px"><span>&#8249;</span><span>&#8250;</span></div>
    <div class="dist-grid">
      <div class="dist-card">
        <div class="dist-photo" role="img" aria-label="Hands working at a desk beside a keyboard and printed papers" style="background:linear-gradient(135deg,#f1f1f1,#c9c9cc 55%,#8a6a58)"></div>
        <h3>PRINT</h3>
        <p>Download PDF certificates to print and physically hand them out or mail them to your customers!</p>
        <span class="btn-line">Read More</span>
      </div>
      <div class="dist-card">
        <div class="dist-photo" role="img" aria-label="Hand holding a tablet with emails flying out on a red background" style="background:linear-gradient(135deg,#c45b66,#e4a4aa 50%,#a8343f)"></div>
        <h3>EMAIL</h3>
        <p>Email e-certificates to your customers individually or in bulk with just one click!</p>
        <span class="btn-line">Read More</span>
      </div>
      <div class="dist-card">
        <div class="dist-photo" role="img" aria-label="Person typing on a laptop at a wooden table" style="background:linear-gradient(135deg,#d9b7a8,#b98e7c 50%,#6f5b55)"></div>
        <h3>ONLINE AUTOMATION</h3>
        <p>Add our web banners on your website. Your customers click on the banner to get their certificate.</p>
        <span class="btn-line">Read More</span>
      </div>
    </div>
  </div>
</section>

<section class="pricing">
  <div class="wrap">
    <h2 class="section-title">Give Away An Unlimited Amount Of Certificates To Your<br>Customers For Just $99 Bucks A Month.</h2>
    <p>We are A rated with the Business Trust Council as well as a licensed seller of travel registered with the State Attorney General (CST# 4470318). We also participate in The Traveler Protection Reserve Fund (TPRF), which was created to protect consumers from unscrupulous travel companies.</p>
    <p>TPRF is a program that requires travel agencies like us to hold a "Passenger Trust Account" and requires that all traveler funds that we collect must be deposited into this account. If a consumer contacts the Attorney General to complain about us for any reason, the Atty General has 100% access to the "Passenger Trust Account" and has the right to take money from the account at any time to give back to the disgruntled consumer.</p>
    <span class="btn-solid">READ MORE INFORMATION</span>
  </div>
</section>

<section class="clients">
  <div class="wrap">
    <h2 class="section-title">Our Clients</h2>
    <div class="client-row">
      <span class="client-arrow" style="left:-34px">&#8249;</span>
      <div class="client-logo">Harbourline Bank</div>
      <div class="client-logo">Southcross Lending</div>
      <div class="client-logo">Unity Federal</div>
      <div class="client-logo">Meridian Trust</div>
      <div class="client-logo">Valuecrest</div>
      <div class="client-logo">Northpeak</div>
      <span class="client-arrow" style="right:-34px">&#8250;</span>
    </div>
  </div>
</section>

<footer class="site-footer">
  <div class="wrap">
    <div class="foot-cols">
      <div class="foot-col links">
        <h4>Quick Links</h4>
        <ul>
          <li>Home</li><li>About Us</li><li>Services</li><li>Blog</li><li>Contact Us</li>
          <li>Terms &amp; Conditions</li><li>Privacy Policy</li><li>FAQ</li><li>Site Map</li>
        </ul>
      </div>
      <div class="foot-col contact">
        <h4>Contact Info</h4>
        <div>1840 Orchard Ridge Road</div>
        <div>Lakeview, CA 92100 CST-4470318</div>
        <div class="row"><svg width="14" height="14" viewBox="0 0 24 24" fill="#fff"><path d="M6.6 10.8a15 15 0 0 0 6.6 6.6l2.2-2.2a1 1 0 0 1 1-.25 11.4 11.4 0 0 0 3.6.6 1 1 0 0 1 1 1V20a1 1 0 0 1-1 1A17 17 0 0 1 3 4a1 1 0 0 1 1-1h3.5a1 1 0 0 1 1 1c0 1.25.2 2.45.6 3.6a1 1 0 0 1-.25 1z"/></svg>1-800-555-0192</div>
        <div class="row"><svg width="14" height="12" viewBox="0 0 24 18" fill="#fff"><path d="M0 0h24v2L12 10 0 2zM0 4l12 8 12-8v14H0z"/></svg>hello@brightlanepromoworks.biz</div>
      </div>
      <div class="foot-col news">
        <h4>Sign Up For Newsletters</h4>
        <p>Please sign up here for latest news</p>
        <div class="sub-form"><span>EMAIL ADDRESS</span><b>SUBSCRIBE</b></div>
        <div class="socials"><span></span><span></span><span></span><span></span></div>
      </div>
    </div>
    <div class="copyright">&copy; 2017 Brightlane Promoworks Group, Inc. . All right reserved . Term of Use</div>
  </div>
</footer>

</body>
</html>
```